Night Dresses business cards business requirers

We are a new company initiating Mexico operations. Our core business is Night woman dress (both formal and party dress) for rent. Gownvella is the name of the company. ITS Gownvella form by two word. The dress word and topia (Utopic) so the place Gownvella Means That You cant get the ideal, perfect and unique dress for your event. So we would like a modern, very creative, and attractive business card.

Industry/Entity Type

Womens Clothing

Contact Information for Business Card

Rounded Borders, two faces

Requirements
Must have
• Rounded borders, logo and slogan, modern, glam, attractive design
Should not have
• modern design classic or not

```html
<!DOCTYPE html>
<html lang="en">
<head>
<meta charset="utf-8">
<title>Gownvella — Business Cards</title>
<link rel="stylesheet" href="https://fonts.googleapis.com/css2?family=Source+Sans+3:wght@400;600&display=swap">
<style>
  :root {
    --page-bg: #2c2c2e;
    --card-white: #fbfbfb;
    --card-black: #0d0d0e;
    --brand-plum: #a24b90;
    --ink: #2a2a2a;
    --silver: #d6d6d8;
    --silver-dim: #a4a4a8;
    --divider: #e6c7dd;
  }
  * { margin: 0; padding: 0; box-sizing: border-box; }
  html, body { width: 1200px; height: 900px; overflow: hidden; }
  body {
    background: var(--page-bg);
    font-family: "Source Sans 3", "Myriad Pro", sans-serif;
    position: relative;
  }
  .card {
    position: absolute;
    top: 307px;
    width: 500px;
    height: 286px;
    border-radius: 22px;
    overflow: hidden;
  }
  /* Front face */
  .card--front { left: 80px; background: var(--card-white); color: var(--ink); }
  .front__brand {
    position: absolute;
    left: 0; top: 0;
    width: 230px; height: 100%;
    display: flex; align-items: center; justify-content: center; gap: 10px;
  }
  .brand-dot {
    width: 20px; height: 20px; border-radius: 50%;
    border: 3px solid var(--brand-plum);
    flex: none;
  }
  .front__brand-name {
    font-size: 26px; font-weight: 600; color: var(--brand-plum);
  }
  .front__divider {
    position: absolute; left: 232px; top: 40px;
    width: 1px; height: 206px;
    background: linear-gradient(to bottom, transparent, var(--divider) 25%, var(--divider) 75%, transparent);
  }
  .front__details {
    position: absolute; left: 252px; top: 44px; right: 20px;
    font-size: 13.5px; line-height: 1.3;
  }
  .person-name {
    font-size: 20px; font-weight: 600; color: var(--brand-plum);
    letter-spacing: 0.5px; text-transform: uppercase; line-height: 1.1;
  }
  .person-role { font-size: 12.5px; margin-bottom: 12px; }
  .contact-list { list-style: none; margin-bottom: 10px; }
  .contact-list li { display: flex; align-items: center; gap: 8px; }
  .contact-icon { width: 10px; height: 10px; fill: var(--brand-plum); flex: none; }
  .address { margin-bottom: 8px; }
  .social-link {
    display: flex; align-items: center; gap: 8px;
    color: var(--brand-plum); font-size: 14px;
  }
  .social-square { width: 12px; height: 12px; background: var(--brand-plum); border-radius: 2px; flex: none; }

  /* Back face */
  .card--back {
    left: 620px; background: var(--card-black);
    display: flex; flex-direction: column; align-items: center; justify-content: center;
  }
  .back__brand {
    display: flex; align-items: center; gap: 12px;
    font-size: 30px; font-weight: 600; color: var(--silver);
  }
  .back__brand .brand-dot { border-color: var(--silver); }
  .back__slogan {
    margin-top: 6px;
    font-size: 14px; font-weight: 400; color: var(--silver-dim);
  }
</style>
</head>
<body>
  <section class="card card--front" aria-label="Business card front">
    <div class="front__brand">
      <span class="brand-dot"></span>
      <span class="front__brand-name">Gownvella</span>
    </div>
    <div class="front__divider"></div>
    <div class="front__details">
      <p class="person-name">Lucia Ferrer</p>
      <p class="person-role">Director</p>
      <ul class="contact-list">
        <li>
          <svg class="contact-icon" viewBox="0 0 10 10"><path d="M2 0.5 L3.6 2.6 L2.7 3.6 Q3.6 5.6 6.4 7.3 L7.4 6.4 L9.5 8 L8.4 9.5 Q3 8.8 0.5 1.6 Z"/></svg>
          <span>(442) 5550187</span>
        </li>
        <li>
          <svg class="contact-icon" viewBox="0 0 10 10"><path d="M0 2 H10 V8.5 H0 Z M0.8 2.6 L5 5.6 L9.2 2.6" stroke="#fff" stroke-width="0.8"/></svg>
          <span>lucia.ferrer@gownvella.mx</span>
        </li>
        <li>
          <svg class="contact-icon" viewBox="0 0 10 10"><circle cx="5" cy="5" r="4.6"/><path d="M0.5 5 H9.5 M5 0.4 Q2.4 5 5 9.6 M5 0.4 Q7.6 5 5 9.6" stroke="#fff" stroke-width="0.7" fill="none"/></svg>
          <span>www.gownvella.mx</span>
        </li>
      </ul>
      <p class="address">Av. Las Palmas 218 - Local 4<br>Colinas, Querétaro, Qro. CP. 76100</p>
      <p class="social-link"><span class="social-square"></span>www.social.com/gownvella</p>
    </div>
  </section>

  <section class="card card--back" aria-label="Business card back">
    <div class="back__brand"><span class="brand-dot"></span>Gownvella</div>
    <p class="back__slogan">Evening gowns to rent</p>
  </section>
</body>
</html>
```